Etiketten-Design für Dankeswein
Zielgruppe
Vo-Lux:
Wir stellen für unsere Kunden einen Dankeswein her. Er soll eine Hommage an die Freundschaft und Partnerschaft sein.
Subtitle, could be, but perhaps not:
When we meet, anything can happen.
Name: Vo-Lux (evtl. Änderung auf KaFol)
Aufgabenstellung
Das Ettikett darf auch bunt sein, aber es sollte vorallem sehr Professionell sein.
Der Wein wird rötlich sein, die Flasche weiss durchsichtig. Es werden wahrscheinlich 0,5l Flaschen.
Die Form des Ettikets, kann noch definiert werden.
Es geht um eine Homage an das Treffen von Menschen und die Freundschaft.
Vo-Lux
Hintergrundinfos, die eher für den Hintergrund, Einarbeitung und kleine Abbildung gedacht sind.
TORVIK: ist eine IT Firma, die von 2 Partnern gegründet wurde. Das Logo sollte mit drauf, evtl. kann man auch sich an diesen Farben orientieren.
Familie Abegg: Die Tiersymbole repräsentieren die beiden Eltern. Das geschwungene H ist das Familienzeichen. Wenn man es rotiert. ähnelt es wieder einem Schmetterling. Vielleicht kann man da grafisch etwas machen?
Das geschwungene H oder die Tiersymbole haben hohen emotionalen Wert. In dem Wappen ist das neue Familiensymbol eingearbeitet in das noch ältere Familienwappen der Familie. Prio hat das geschwungene H
Für das Ettikett gibt es leider rechtliche Pflichtangaben:
TORVIK GmbH
Rindermarktgasse 9 CH-4052 Basel
Erzeugerab füllung:D- RP 7 438 926
A.P.-Nr.7 438 926 XXXX
11,0%vol 50 cl Enthält Sulfite
Deutscher Qualitätswein – Mosel
vo-lux.eu

```html
<!DOCTYPE html>
<html lang="de">
<head>
<meta charset="utf-8">
<title>Vo-Lux – Dankeswein Etikett</title>
<link rel="stylesheet" href="https://fonts.googleapis.com/css2?family=Bebas+Neue&family=Roboto+Condensed:wght@400;700&display=swap">
<style>
  :root {
    --canvas-bg: #ece7e2;
    --label-black: #0b0b0c;
    --label-edge: #2a2a2c;
    --sky-blue: #3fa4dc;
    --teal: #3cb8c0;
    --leaf-green: #8cc63e;
    --soft-grey: #8a8a8e;
    --arrow-grey: #6b6b70;
    --rule-white: #f2f2f2;
    --maker-blue: #5b8fb8;
  }
  html, body {
    margin: 0;
    padding: 0;
    width: 1200px;
    height: 2748px;
    overflow: hidden;
    background: var(--canvas-bg);
  }
  .canvas {
    position: relative;
    width: 1200px;
    height: 2748px;
  }
  .wine-label {
    position: absolute;
    left: 150px;
    top: 700px;
    width: 900px;
    height: 1330px;
    background: var(--label-black);
    border: 6px solid var(--label-edge);
    border-radius: 56px;
    box-sizing: border-box;
    overflow: hidden;
  }
  .butterfly-area {
    position: absolute;
    left: 500px;
    top: 250px;
    width: 300px;
    height: 230px;
    border-radius: 24px;
    background: linear-gradient(135deg, var(--leaf-green) 0%, var(--teal) 55%, var(--sky-blue) 100%);
    opacity: 0.85;
  }
  .tagline {
    position: absolute;
    left: 106px;
    top: 498px;
    margin: 0;
    font-family: "Roboto Condensed", sans-serif;
    font-weight: 400;
    font-size: 30px;
    line-height: 36px;
    letter-spacing: 3px;
    color: var(--soft-grey);
    text-transform: uppercase;
  }
  .title {
    position: absolute;
    left: 118px;
    top: 640px;
    margin: 0;
    font-family: "Bebas Neue", sans-serif;
    font-weight: 400;
    font-size: 228px;
    line-height: 210px;
    letter-spacing: 4px;
  }
  .title-when { display: block; color: var(--sky-blue); }
  .title-name { display: block; color: var(--leaf-green); }
  .title-rule {
    position: absolute;
    left: 354px;
    top: 1120px;
    width: 150px;
    height: 6px;
    background: var(--rule-white);
  }
  .arrow-trail {
    position: absolute;
    left: 700px;
    top: 640px;
    width: 120px;
    height: 580px;
  }
  .maker-name {
    position: absolute;
    left: 0;
    right: 0;
    top: 1222px;
    margin: 0;
    text-align: center;
    font-family: "Roboto Condensed", sans-serif;
    font-weight: 700;
    font-size: 34px;
    letter-spacing: 4px;
    color: var(--maker-blue);
  }
</style>
</head>
<body>
<main class="canvas">
  <section class="wine-label" aria-label="Weinetikett Vo-Lux">
    <div class="butterfly-area" role="img" aria-label="Platz für den bunten Schmetterling in Grün, Türkis und Blau"></div>

    <p class="tagline">Anything<br>can happen</p>

    <h1 class="title">
      <span class="title-when">When</span>
      <span class="title-name">Vo-Lux</span>
    </h1>
    <div class="title-rule"></div>

    <svg class="arrow-trail" viewBox="0 0 120 580" aria-hidden="true">
      <g fill="none" stroke="var(--arrow-grey)" stroke-width="5" stroke-linecap="round" stroke-linejoin="round">
        <path d="M20 40 Q 60 10 95 30"/><path d="M80 18 L95 30 L78 40"/>
        <path d="M15 150 Q 55 175 95 145"/><path d="M82 140 L95 145 L88 160"/>
        <path d="M20 265 Q 60 240 95 262"/><path d="M80 250 L95 262 L78 272"/>
        <path d="M15 390 Q 55 415 95 385"/><path d="M82 380 L95 385 L88 400"/>
        <path d="M20 540 Q 60 515 95 537"/><path d="M80 525 L95 537 L78 547"/>
      </g>
    </svg>

    <p class="maker-name">TORVIK</p>
  </section>
</main>
</body>
</html>
```